COMPANY NAME ------ Velmora82 Brands, Inc. TAGLINE......... It's Splendor!

I need Graphic design for Coconut oil Skincare products!
I need a graphic design that portrays LUXURY AS APPLIED TO MY COMPANY AND THE TAGLINE ! UPSCALE!!
COLOR LAYOUT ................. GOLD ON BLACK, GOLD ON CHOCOLATE LIKE COLOR!
The designers can focus their graphic design based more the word.." "LUXURY"..... The logo I submitted is the two logo I picked.. the logo and the slogan has to be incorporated in the graphic design... The label has to be "ELEGANT" and " UPSCALE".. It can also be "BOLD".

Target Market(s)

20 - 45 years

Industry/Entity Type

Graphic Design

Font styles to use
Decorative

Requirements
Must have
• Luxury feel to it....
Nice to have
• Logo on the label and oil pouring from inside Coconuts !
Should not have
• Local or Country feel because of the word Coconut oil

```html
<!DOCTYPE html>
<html lang="en">
<head>
<meta charset="utf-8">
<title>Velmora82 — Luma Luma Coconut Oil Label</title>
<link rel="stylesheet" href="https://fonts.googleapis.com/css2?family=Libre+Baskerville:wght@700&family=Poiret+One&display=swap">
<style>
  :root {
    --chocolate: #2a0f0a;
    --chocolate-deep: #1f0a06;
    --gold: #d9a441;
    --gold-light: #f6dc8e;
    --gold-dark: #a8701f;
  }
  html, body {
    margin: 0;
    padding: 0;
    overflow: hidden;
    background: var(--chocolate-deep);
  }
  .label {
    position: relative;
    width: 800px;
    height: 1200px;
    overflow: hidden;
    background: radial-gradient(ellipse at 50% 45%, var(--chocolate) 0%, var(--chocolate-deep) 100%);
  }
  .brand {
    position: absolute;
    left: 0;
    right: 0;
    top: 305px;
    text-align: center;
    font-family: "Libre Baskerville", Georgia, serif;
    font-weight: 700;
    color: var(--gold);
  }
  .brand-name {
    margin: 0;
    font-size: 37px;
    line-height: 1.1;
    letter-spacing: 1px;
  }
  .brand-tagline {
    margin: 4px 0 0;
    font-size: 19px;
    line-height: 1.2;
    letter-spacing: 1px;
  }
  .product-title {
    position: absolute;
    left: 0;
    right: 0;
    top: 455px;
    margin: 0;
    text-align: center;
    font-family: "Poiret One", "Didot", sans-serif;
    font-weight: 400;
    line-height: 1;
    background: linear-gradient(180deg, var(--gold-light) 0%, var(--gold) 55%, var(--gold-dark) 100%);
    -webkit-background-clip: text;
    background-clip: text;
    color: transparent;
  }
  .product-title span {
    display: block;
  }
  .product-name {
    font-size: 122px;
    letter-spacing: 4px;
  }
  .product-type {
    font-size: 100px;
    letter-spacing: 2px;
    margin-top: 14px;
  }
  .product-kind {
    font-size: 100px;
    letter-spacing: 2px;
    margin-top: 14px;
  }
  .coconut-art {
    position: absolute;
    left: 274px;
    top: 886px;
    width: 252px;
    height: 254px;
  }
</style>
</head>
<body>
  <main class="label">
    <header class="brand">
      <p class="brand-name">Velmora82</p>
      <p class="brand-tagline">It's Splendor!</p>
    </header>

    <h1 class="product-title">
      <span class="product-name">LUMA LUMA</span>
      <span class="product-type">COCONUT</span>
      <span class="product-kind">OIL</span>
    </h1>

    <svg class="coconut-art" viewBox="0 0 252 254" role="img" aria-label="Gold illustration of a whole coconut, a halved coconut and a small bottle of oil">
      <defs>
        <radialGradient id="coconutGold" cx="50%" cy="45%" r="60%">
          <stop offset="0%" stop-color="#f6dc8e"/>
          <stop offset="60%" stop-color="#d9a441"/>
          <stop offset="100%" stop-color="#8a5a18" stop-opacity="0.6"/>
        </radialGradient>
      </defs>
      <rect width="252" height="254" rx="40" fill="url(#coconutGold)" opacity="0.55"/>
    </svg>
  </main>
</body>
</html>
```